Homepage Redesign - Hi-tech business Law Firm

I'm looking for an updated graphic design (pdf file) for the homepage of dorvantlegal.ca (and which will form the general template of the other pages - but you don't need to design that). Detailed specs are in the Word file.

Deliverable is 1 pdf file that I find good looking, that sets forth the layout of the new page.

Target Market(s)

Sophisticated customers

Industry/Entity Type

Legal

Number of Pages Required

1 page

Requirements
Nice to have
• For a main background, tech type images to do with high powered boardrooms, computers, graphs, numbers, high tech manufacturing lines etc. Also, I tend to like blues and light greys, and uploaded a file today that shows my generally preferred layout, which a few of you have been getting close to.
Should not have
• Any mention of 'Personal Injury,' backgrounds that include books, or buildings with roman columns. Page should not be in dark colors or harsh on the eyes.

```html
<!DOCTYPE html>
<html lang="en">
<head>
<meta charset="utf-8">
<title>Dorvant Legal — Hi-tech Business Law</title>
<link href="https://fonts.googleapis.com/css2?family=Roboto:wght@400;500;700&display=swap" rel="stylesheet">
<style>
:root{
  --blue:#2a72c4;
  --blue-dark:#1d5aa3;
  --blue-deep:#174a8a;
  --ink:#111418;
  --hero-bg:#1c1d20;
  --grey:#e9edf2;
  --text:#3b4350;
  --white:#ffffff;
}
*{box-sizing:border-box;margin:0;padding:0}
html,body{width:1200px;height:5292px;overflow:hidden}
body{font-family:'Roboto',Arial,sans-serif;color:var(--ink);background:var(--white);position:relative}
section,header,footer{position:absolute;left:0;width:1200px}
.abs{position:absolute}
.btn{display:inline-block;font-size:15px;padding:11px 22px;border:1px solid currentColor;border-radius:2px;margin-right:10px}
.btn-solid{background:var(--blue);border-color:var(--blue);color:var(--white)}
.btn-ghost{color:inherit;background:transparent}

/* nav */
.site-nav{top:0;height:48px;background:var(--white);display:flex;align-items:center;padding:0 20px;border-bottom:1px solid #e3e6ea}
.brand{display:flex;align-items:center;gap:8px;font-weight:700;font-size:17px;color:var(--ink)}
.brand-mark{width:26px;height:26px;background:var(--ink)}
.nav-links{margin-left:auto;display:flex;align-items:center;gap:22px;font-size:14px;color:var(--text)}
.nav-links .btn{font-size:13px;padding:7px 14px;margin:0}
.nav-links .learn{color:var(--blue)}

/* hero */
.hero{top:48px;height:760px;background:var(--hero-bg);color:var(--white)}
.hero h1{left:52px;top:330px;width:520px;font-size:46px;line-height:1.15;font-weight:700}
.hero p{left:52px;top:560px;width:500px;font-size:16px;line-height:1.5;color:#d8dbe0}
.hero .actions{left:52px;top:640px}
.hero-photo{left:580px;top:108px;width:560px;height:560px;border-radius:50%;border:12px solid var(--blue);background:radial-gradient(circle at 50% 40%,#9aa3ae,#3d4a5c)}

/* expertise band */
.expertise{top:808px;height:720px;background:var(--blue);color:var(--white)}
.expertise .intro{left:52px;top:180px;width:560px}
.expertise h2{font-size:33px;line-height:1.2;font-weight:700;margin-bottom:22px}
.expertise .lead{width:500px;font-size:15px;line-height:1.6}
.feature{width:230px;font-size:13px;line-height:1.5}
.feature svg{display:block;margin-bottom:10px}
.feature h3{font-size:16px;font-weight:700;margin-bottom:6px}
.work-photo{left:632px;top:96px;width:520px;height:528px;border-radius:0 0 0 300px;background:linear-gradient(135deg,#f2f3f4,#b9c0c8)}

/* leading */
.leading{top:1528px;height:720px}
.eyebrow{font-size:14px;font-weight:700;color:var(--blue)}
.leading .eyebrow{left:52px;top:192px}
.leading h2{left:52px;top:224px;width:520px;font-size:44px;line-height:1.15;color:var(--blue);font-weight:700}
.leading p{left:52px;top:356px;width:500px;font-size:15px;line-height:1.6;color:var(--text)}
.leading .actions{left:52px;top:480px;display:flex;align-items:center;font-size:15px}
.leading .btn-ghost{color:var(--ink);border-color:#bfc5cc}
.link-arrow{display:flex;align-items:center;gap:8px;margin-left:12px}
.portrait-frame{left:632px;top:64px;width:520px;height:600px;background:var(--blue)}
.portrait{left:660px;top:92px;width:490px;height:540px;border-radius:50%;background:radial-gradient(circle at 50% 40%,#a7aeb8,#3a4658)}

/* clients */
.clients{top:2248px;height:312px;background:linear-gradient(120deg,#1f63b4,#2f80d6 50%,#1d5aa3);color:var(--white);text-align:center}
.clients .caption{top:56px;left:0;width:1200px;font-size:15px;font-weight:500}
.logo-row{left:0;width:1200px;display:flex;justify-content:center;gap:60px;font-size:24px;font-weight:700}
.logo-row span{display:flex;align-items:center;gap:8px}
.logo-row i{width:14px;height:14px;background:var(--white);display:inline-block}

/* testimonial */
.testimonial{top:2560px;height:540px;text-align:center}
.testimonial .client{top:72px;left:0;width:1200px;display:flex;justify-content:center;align-items:center;gap:8px;font-size:20px;font-weight:700;color:var(--blue)}
.testimonial .client i{width:14px;height:14px;background:var(--blue);display:inline-block}
.testimonial blockquote{top:140px;left:260px;width:680px;font-size:22px;line-height:1.5;font-weight:700;color:var(--blue)}
.avatar{top:256px;left:580px;width:40px;height:40px;border-radius:50%;background:#f2a03d}
.testimonial .name{top:306px;left:0;width:1200px;font-size:14px;line-height:1.5}

/* cta */
.cta{top:3100px;left:52px;width:1096px;height:320px;background:var(--blue);border:4px solid #8fb6e6;color:var(--white)}
.cta h2{left:52px;top:52px;width:560px;font-size:38px;line-height:1.2;font-weight:700}
.cta p{left:52px;top:160px;font-size:15px}
.cta .actions{left:52px;top:216px}
.btn-dark{background:#000;border-color:#000;color:var(--white)}

/* newsletter */
.newsletter{top:3540px;height:440px}
.newsletter h2{left:52px;top:100px;width:520px;font-size:40px;line-height:1.2;color:var(--blue);font-weight:700}
.newsletter p{left:52px;top:212px;width:500px;font-size:16px;line-height:1.5;color:var(--text)}
.signup{left:52px;top:296px;display:flex;gap:12px}
.signup .field{width:320px;height:44px;border:1px solid #bfc5cc;font-size:14px;color:#8a929c;padding:13px 14px}
.signup .btn{margin:0;height:44px}
.fine{left:52px;top:352px;font-size:11px;color:var(--text)}
.fine u{color:var(--ink)}
.statue-photo{left:632px;top:64px;width:520px;height:360px;background:linear-gradient(135deg,#d9d6d0,#8f8a84)}

/* contact */
.contact{top:3980px;height:860px}
.contact .eyebrow{left:52px;top:36px}
.contact h2{left:52px;top:64px;font-size:44px;font-weight:700;color:var(--blue)}
.contact .sub{left:52px;top:138px;font-size:15px;color:var(--text)}
.contact-item{left:52px;width:360px;font-size:14px;line-height:1.6;color:var(--text)}
.contact-item h3{font-size:18px;color:var(--ink);margin:10px 0 4px;font-weight:700}
.contact-item a{color:var(--ink);text-decoration:underline}
.map{left:452px;top:188px;width:700px;height:552px;background:linear-gradient(135deg,#e2d4b3,#c9ae7f 60%,#b58e5c)}

/* footer */
.site-footer{top:4840px;height:452px;background:var(--blue);color:var(--white)}
.site-footer .brand{position:absolute;left:52px;top:56px;color:var(--white);font-size:22px}
.foot-col{top:56px;width:150px;font-size:13px;line-height:2.1}
.foot-col h4{font-size:14px;font-weight:700;margin-bottom:6px}
.subscribe{left:724px;top:56px;width:424px;font-size:13px;line-height:1.5}
.subscribe h4{font-size:14px;margin-bottom:10px}
.subscribe .row{display:flex;gap:12px;margin:18px 0 12px}
.subscribe .field{flex:1;height:44px;background:var(--white)}
.subscribe .btn{margin:0;color:var(--white);border-color:var(--white)}
.subscribe small{font-size:11px}
.foot-rule{left:52px;top:300px;width:1096px;height:1px;background:rgba(255,255,255,.6)}
.legal{left:52px;top:324px;font-size:12px;display:flex;gap:26px}
.legal span+span{text-decoration:underline}
.social{left:1000px;top:320px;display:flex;gap:14px}
.social i{width:18px;height:18px;border-radius:50%;background:var(--white);display:block}
</style>
</head>
<body>

<header class="site-nav">
  <div class="brand"><span class="brand-mark"></span>Dorvant Legal</div>
  <nav class="nav-links">
    <span>About Us</span><span>Services</span><span>Contact</span><span>More &#9662;</span>
    <span class="btn btn-ghost learn">Learn</span>
    <span class="btn btn-solid">Sign Up</span>
  </nav>
</header>

<section class="hero">
  <h1 class="abs">Specializing in hi-tech legal solutions for businesses</h1>
  <p class="abs">We combine our expertise in law and technology to provide innovative solutions that meet the unique needs of hi-tech businesses.</p>
  <div class="abs actions"><span class="btn btn-solid">Learn More</span><span class="btn btn-ghost">Sign Up</span></div>
  <div class="abs hero-photo" role="img" aria-label="Portrait of a bearded lawyer in a dark suit"></div>
</section>

<section class="expertise">
  <div class="abs intro">
    <h2>Experience Expertise and Results<br>in Hi-Tech Business Law</h2>
    <p class="lead">Our law firm specializes in providing comprehensive legal solutions for hi-tech businesses. With our deep understanding of the industry and track record of success, we are well-equipped to handle all your legal needs.</p>
  </div>
  <div class="abs feature" style="left:52px;top:412px">
    <svg width="32" height="32" viewBox="0 0 32 32"><path d="M16 3 28 9v14L16 29 4 23V9z" fill="#fff"/></svg>
    <h3>Expertise</h3>Our team of experienced attorneys has a proven track record of success in hi-tech business law.
  </div>
  <div class="abs feature" style="left:316px;top:412px">
    <svg width="32" height="32" viewBox="0 0 32 32"><path d="M16 3 28 9v14L16 29 4 23V9z" fill="#fff"/></svg>
    <h3>Results</h3>We are committed to achieving favorable outcomes for our clients in every case.
  </div>
  <div class="abs work-photo" role="img" aria-label="Top view of a person working on a laptop at a white desk with coffee"></div>
</section>

<section class="leading">
  <div class="abs eyebrow">Expertise</div>
  <h2 class="abs">Leading the Way in Tech Industry Success</h2>
  <p class="abs">At our law firm, we have a proven track record of achieving success in the tech industry. Our team of experienced lawyers has helped numerous businesses navigate complex legal challenges and secure favorable outcomes. Trust us to provide you with the legal expertise you need to thrive in the ever-evolving tech landscape.</p>
  <div class="abs actions">
    <span class="btn btn-ghost">Learn More</span>
    <span class="link-arrow">Contact Us
      <svg width="18" height="18" viewBox="0 0 18 18"><circle cx="9" cy="9" r="9" fill="var(--blue)"/><path d="M7 5l4 4-4 4" stroke="#fff" stroke-width="2" fill="none"/></svg></span>
  </div>
  <div class="abs portrait-frame"></div>
  <div class="abs portrait" role="img" aria-label="Portrait of a smiling lawyer in a suit and blue tie"></div>
</section>

<section class="clients" role="region" aria-label="Client companies over a blue city skyline backdrop">
  <div class="abs caption">Trusted by industry leading companies around the globe</div>
  <div class="abs logo-row" style="top:120px"><span><i></i>Northwave</span><span><i></i>Kestrel</span><span><i></i>Northwave</span><span><i></i>Kestrel</span><span><i></i>Northwave</span></div>
  <div class="abs logo-row" style="top:184px"><span><i></i>Northwave</span><span><i></i>Kestrel</span><span><i></i>Northwave</span><span><i></i>Kestrel</span><span><i></i>Kestrel</span><span><i></i>Northwave</span></div>
</section>

<section class="testimonial">
  <div class="abs client"><i></i>Northwave</div>
  <blockquote class="abs">"The law firm's legal expertise helped me navigate a complex business dispute and achieve a favorable outcome. Their dedication and professionalism are unmatched."</blockquote>
  <div class="abs avatar"></div>
  <div class="abs name"><strong>John Doe</strong><br>CEO, Corvix Systems</div>
</section>

<section class="cta">
  <h2 class="abs">Transforming Businesses with Legal Expertise</h2>
  <p class="abs">Our team of experienced lawyers will guide you through complex legal matters.</p>
  <div class="abs actions"><span class="btn btn-dark">Schedule</span><span class="btn btn-ghost">Consultation</span></div>
</section>

<section class="newsletter">
  <h2 class="abs">Medium length heading goes here</h2>
  <p class="abs">Lorem ipsum dolor sit amet, consectetur adipiscing elit. Suspendisse varius enim in eros elementum tristique.</p>
  <div class="abs signup"><div class="field">Placeholder</div><span class="btn btn-solid">Button</span></div>
  <div class="abs fine">By clicking Sign Up you're confirming that you agree with our <u>Terms and Conditions</u>.</div>
  <div class="abs statue-photo" role="img" aria-label="Bronze statue of Lady Justice holding scales against a stone wall"></div>
</section>

<section class="contact">
  <div class="abs eyebrow">Innovation</div>
  <h2 class="abs">Contact Information</h2>
  <div class="abs sub">For any inquiries, please feel free to reach out to us.</div>
  <div class="abs contact-item" style="top:220px">
    <svg width="24" height="24" viewBox="0 0 24 24"><rect x="2" y="5" width="20" height="14" fill="none" stroke="var(--blue)" stroke-width="2"/><path d="M2 5l10 8 10-8" fill="none" stroke="var(--blue)" stroke-width="2"/></svg>
    <h3>Email</h3>Send us an email today!<br><a>hello@dorvantlegal.ca</a>
  </div>
  <div class="abs contact-item" style="top:372px">
    <svg width="24" height="24" viewBox="0 0 24 24"><path d="M6 2h4l2 5-3 2a12 12 0 006 6l2-3 5 2v4a2 2 0 01-2 2A18 18 0 014 4a2 2 0 012-2z" fill="var(--blue)"/></svg>
    <h3>Phone</h3>Call us for assistance.<br><a>+1 (555) 014-2290</a>
  </div>
  <div class="abs contact-item" style="top:524px">
    <svg width="24" height="24" viewBox="0 0 24 24"><path d="M12 2a7 7 0 017 7c0 5-7 13-7 13S5 14 5 9a7 7 0 017-7z" fill="var(--blue)"/><circle cx="12" cy="9" r="2.5" fill="#fff"/></svg>
    <h3>Office</h3>48 Harbour Lane, Toronto ON M5V 2T6
  </div>
  <div class="abs link-arrow" style="left:40px;top:736px;font-size:14px">Button
    <svg width="18" height="18" viewBox="0 0 18 18"><circle cx="9" cy="9" r="9" fill="var(--blue)"/><path d="M7 5l4 4-4 4" stroke="#fff" stroke-width="2" fill="none"/></svg></div>
  <div class="abs map" role="img" aria-label="Antique world map in warm parchment tones"></div>
</section>

<footer class="site-footer">
  <div class="brand">Dorvant Legal</div>
  <div class="abs foot-col" style="left:200px"><h4>About Us</h4>Contact<br>Services<br>Blog<br>FAQ<br>Support</div>
  <div class="abs foot-col" style="left:356px"><h4>Terms</h4>Privacy<br>Sitemap<br>Careers<br>Partners<br>Investors</div>
  <div class="abs foot-col" style="left:504px"><h4>News</h4>Events<br>Support<br>Documents<br>Community<br>Tutorials</div>
  <div class="abs subscribe"><h4>Subscribe</h4>Stay up to date with our latest features and releases.
    <div class="row"><div class="field"></div><span class="btn">Button</span></div>
    <small>By subscribing, you agree to our Privacy Policy and consent to receive updates from our company.</small></div>
  <div class="abs foot-rule"></div>
  <div class="abs legal"><span>© 2023 Dorvant Legal. All rights reserved.</span><span>Privacy Policy</span><span>Terms of Service</span><span>Cookie Settings</span></div>
  <div class="abs social"><i></i><i></i><i></i><i></i><i></i></div>
</footer>

</body>
</html>
```